wine label design

i'm a fine wine store based in new zealand which buys quality bulk wine and bottles it, passing on the significant savings onto the customer. i require a brand name and design which is cool/ sharp and contempory. the wines will be all still wines, there won't be any sparkling wines under this brand. i've used brand names like harbourlight wine company for previous designs/label but want something more edgier. we thought about a brand name 'sky above the vines' or 'harbourlight wine co' but couldn't get a design to match the title of brand, if you have any thoughts on this send thru your design. take into account color they have to be bold as i am printing these thru a digital printer. the label is a wrap around design, the dimensions are approximately 80 or 90 mm high and 210 mm wide. have a look at these links, i think they have some x-factor to them: http://www.marlowvale.example/store/product_images/p/855/velora__34476_zoom.jpg: OR

http://static3.cellarfinder.example/images/labels/35/24/ember-in-the-fog-shiraz-petite-sirah-south-australia-10203524.jpg: OR

http://www.bottlebarn.example/ui/productimages/25223/25223_w240.jpg: OR

http://www.vintrail.example/images/viewWinery.php?pic=238291

Take into account i have to be able put a wine desription on the back label, barcode and a few technical details required by law. on the front label all i require is space to put the grape variety, area and vintage. i need the grape type to really stand out.
Updates

Reason: hi, the designs coming thru look good, just need a little more changes, also please read thru the brief, there are a few things i have noted such as label size etc etc

Target Market(s)

am after a label the cool/edgy/contempoary that appeals to the educated well off customer that willing to give something new a go by the look of the label that is cool and edgy.

Industry/Entity Type

Boutique

Requirements
Must have
• bold bold bold, it must stand out on the shelf
Nice to have
• a title/brand name that links what i'm doing, from what i'm doing the name 'harbourlight wine co' is probably best suited.
Should not have
• basic boring artwork and small text, the bigger the text the better

```html
<!DOCTYPE html>
<html lang="en">
<head>
<meta charset="utf-8">
<title>Harbourlight Wine Co — Wrap Label</title>
<link rel="stylesheet" href="https://fonts.googleapis.com/css2?family=Archivo:wght@400;600;700;800&family=Oswald:wght@500;600&display=swap">
<style>
  :root {
    --page: #ffffff;
    --label-light: #f1f1ee;
    --label-dark: #dcdcd8;
    --ink: #141414;
    --ink-mid: #2a2a2a;
    --rule: #8a8a8a;
    --accent-red: #c4161c;
  }
  * { box-sizing: border-box; margin: 0; padding: 0; }
  html, body {
    width: 804px; height: 1200px; overflow: hidden;
    background: var(--page);
    font-family: "Archivo", Arial, sans-serif;
    color: var(--ink);
  }
  .canvas { position: relative; width: 804px; height: 1200px; }

  .label {
    position: absolute;
    background: linear-gradient(100deg, var(--label-light) 0%, var(--label-light) 45%, var(--label-dark) 100%);
    box-shadow: 0 0 0 1px #e2e2de;
  }

  /* Front label */
  .front-label { left: 52px; top: 150px; width: 700px; height: 350px; }
  .brand {
    position: absolute; left: 0; right: 0; top: 62px;
    text-align: center;
  }
  .brand-name {
    font-weight: 800; font-size: 82px; letter-spacing: -2px; line-height: 1;
    color: var(--ink);
  }
  .brand-sub {
    display: block; text-align: right; padding-right: 118px; margin-top: 2px;
    font-weight: 800; font-size: 22px; color: var(--ink); letter-spacing: 1px;
  }
  .vintage {
    position: absolute; left: 0; right: 0; top: 188px;
    display: flex; justify-content: center; align-items: center; gap: 12px;
  }
  .vintage-rule { width: 34px; height: 3px; background: var(--accent-red); }
  .vintage-word {
    font-family: "Oswald", Impact, sans-serif; font-weight: 600;
    font-size: 24px; letter-spacing: 2px; color: var(--accent-red); line-height: 1.2;
  }
  .variety {
    position: absolute; left: 0; right: 0; top: 228px;
    text-align: center;
    font-weight: 800; font-size: 34px; letter-spacing: 1px; line-height: 1.1;
    text-transform: uppercase; color: var(--ink);
  }
  .front-origin {
    position: absolute; left: 0; right: 0; top: 274px;
    text-align: center;
    font-weight: 700; font-size: 14px; letter-spacing: 2px; line-height: 1.3;
    text-transform: uppercase; color: var(--ink-mid);
  }
  .front-footer {
    position: absolute; left: 22px; right: 22px; bottom: 14px;
    display: flex; justify-content: space-between;
    font-weight: 700; font-size: 10px; letter-spacing: 1px; text-transform: uppercase; color: var(--ink);
  }

  /* Back label */
  .back-label { left: 212px; top: 580px; width: 380px; height: 380px; padding: 24px 26px; }
  .back-brand { font-weight: 800; font-size: 26px; letter-spacing: -0.5px; line-height: 1; }
  .back-brand small { display: block; font-size: 11px; letter-spacing: 1px; margin-top: 2px; }
  .back-details {
    margin-top: 10px; font-weight: 700; font-size: 9.5px; line-height: 1.55; letter-spacing: 1px;
    text-transform: uppercase; color: var(--ink-mid);
  }
  .back-divider { height: 1px; background: var(--rule); margin: 14px 0 10px; }
  .back-description { font-weight: 600; font-size: 9.5px; line-height: 1.5; color: var(--ink-mid); }
  .back-volume { margin-top: 16px; font-weight: 800; font-size: 26px; line-height: 1; }
  .back-legal { margin-top: 4px; font-weight: 700; font-size: 8.5px; letter-spacing: 0.5px; color: var(--ink-mid); }
  .back-bottler {
    margin-top: 12px; font-weight: 700; font-size: 8.5px; line-height: 1.6; letter-spacing: 0.5px;
    text-transform: uppercase; color: var(--ink-mid);
  }
  .back-web {
    position: absolute; left: 0; right: 0; bottom: 14px; text-align: center;
    font-weight: 700; font-size: 9px; letter-spacing: 1px; color: var(--ink-mid);
  }
</style>
</head>
<body>
<main class="canvas">

  <section class="label front-label" aria-label="Front label">
    <div class="brand">
      <div class="brand-name">Harbourlight</div>
      <span class="brand-sub">wine co</span>
    </div>
    <div class="vintage">
      <span class="vintage-rule"></span>
      <span class="vintage-word">VINTAGE</span>
      <span class="vintage-rule"></span>
    </div>
    <p class="variety">Sauvignon Blanc</p>
    <p class="front-origin">Marlborough · New Zealand · 2007</p>
    <div class="front-footer">
      <span>Bottled by Harbourlight Wine Co · New Zealand</span>
      <span>750 ML · ALC. 13.5% BY VOL.</span>
    </div>
  </section>

  <section class="label back-label" aria-label="Back label">
    <div class="back-brand">Harbourlight<small>wine co</small></div>
    <p class="back-details">Sauvignon Blanc<br>Marlborough Region<br>New Zealand<br>2007 Vintage</p>
    <div class="back-divider"></div>
    <p class="back-description">Sourced from a single parcel of fruit and bottled here at our cellar, this wine offers bright citrus, passionfruit and fresh cut herbs with a crisp, lingering finish. Enjoy now or cellar for two years.</p>
    <p class="back-volume">750 ML</p>
    <p class="back-legal">13.5% ALC/VOL · 7.9 STD DRINKS</p>
    <p class="back-bottler">Bottled by Harbourlight Wine Co<br>New Zealand wine · Product of<br>New Zealand</p>
    <p class="back-web">www.harbourlightwine.example</p>
  </section>

</main>
</body>
</html>
```